依頼詳細
■デザインのみになります。コーディング・設置は必要ありません。

ターゲットの方々が経営者や弁護士・医師の方々ですので、シックな雰囲気や高級感のあるテイストを希望しています。あまりごちゃごちゃしない方がいいです。そしてPC表示とスマートフォン表示は別のものを用意していただきたいと思っています。その辺りは以下のサイトを参照してください。

https://ka-gakuin.example/lp1/

ファッション系のサービスなので、デザインにも、そこそここだわりたいと思っています。指標となるデザインは以下を参照してください。このようなテイストが個人的に好みです。あくまで参考程度に。

https://www.verdalune.example/
https://www.shokumalink.example/user/landing/general01
https://shigoto-meijin.example/

それではみなさんからのご提案を楽しみにしております。どうぞ宜しくお願いいたします。※デザインのみになります。コーディングは必要ありません。
サイトURL
http://kiriharada.example/
ページ数
5ページ
希望イメージ
シンプル 複雑
単色 カラフル
暗い 明るい
日常 高級
遊び心 厳粛
未来的 伝統的
女性的 男性的
希望する色
青系、茶系、グレー系
納品ファイル
• フォトショップ形式 (.psd)
• PNG形式 (.png)
補足説明
・ホームページとスマートフォンでデザインが最適化されることを望んでいます。
・原稿は「添付ファイル」を参照してください。
・写真素材はこちらからダウンロードをお願いします。
http://22.filebako.example/0617-x7k29d41m3p8q05r6t2w9y4z8c1v7n3b5
■LPは縦長の1ページでお願いします
■文章量は添付ファイルをご確認ください
■ページ数が5ページとなっていますが、制作は縦長の1ページでお願いします。それなりに文章量がありますので、5ページという形で表現しています。
写真素材は以下からダウンロードしてください。http://26.filebako.example/0624-h4j8l2n6p0r3t7v1x5z9b2d6f0g4k8m1q(ギガファイル便6月24日まで)
■ 選んだ理由

センスの良さが際立っていました。ファッション分野のLPなので、細部にまで満足のいくデザインに巡り会えたのはとてもありがたいことだと感じています。

■ 提案者全員のお礼・コメント

この度は優れたデサインを多数ご提案いただきまして、誠にありがとうございました。レベルが高く、選ぶのが大変でしたがとても満足のいくコンペになりました。また機会がありましたら宜しくお願いいたします。

```html
<!DOCTYPE html>
<html lang="ja">
<head>
<meta charset="utf-8">
<title>経営者のための専属スタイリストサービス</title>
<link href="https://fonts.googleapis.com/css2?family=Noto+Serif+JP:wght@400;600;700&family=Noto+Sans+JP:wght@400;500;700&family=Cormorant+Garamond:ital,wght@1,400;1,500&display=swap" rel="stylesheet">
<style>
:root{
  --navy:#1e2242;
  --navy-mid:#393d5a;
  --gold:#a8894b;
  --gold-light:#c8ad72;
  --ink:#2a2a2e;
  --muted:#6b6b72;
  --paper:#ffffff;
  --cream:#f3f1ec;
  --line:#c9c5bb;
}
*{margin:0;padding:0;box-sizing:border-box}
html,body{width:1200px;height:4592px;overflow:hidden}
body{font-family:"Noto Sans JP",sans-serif;color:var(--ink);background:var(--paper);position:relative}
section{position:absolute;left:0;width:1200px;overflow:hidden}
.serif{font-family:"Noto Serif JP",serif}
.en-label{font-family:"Cormorant Garamond",serif;font-style:italic;font-size:26px;letter-spacing:2px;display:flex;align-items:center;justify-content:center;gap:18px}
.en-label::before,.en-label::after{content:"";width:60px;height:1px;background:currentColor;opacity:.6}
.photo{position:absolute}
.section-title{font-family:"Noto Serif JP",serif;font-weight:600;text-align:center;font-size:40px;letter-spacing:2px}
.chevron{position:absolute;left:585px;width:30px;height:18px}

/* hero */
.hero{top:0;height:600px;background:linear-gradient(100deg,#3b3a3c,#5a554f 45%,#7a7064)}
.hero .photo{inset:0;background:linear-gradient(90deg,rgba(40,38,40,.55),rgba(70,64,58,.25) 50%,rgba(90,82,72,.5))}
.hero-tag{position:absolute;top:130px;left:50%;transform:translateX(-50%);background:#fff;color:var(--navy);font-size:17px;padding:8px 26px;font-weight:500;letter-spacing:1px;white-space:nowrap}
.hero-title{position:absolute;top:180px;width:100%;text-align:center;color:#fff;font-family:"Noto Serif JP",serif;font-weight:700;font-size:66px;line-height:1.35;letter-spacing:4px}
.hero-sub{position:absolute;top:370px;width:100%;text-align:center;color:#fff;font-size:22px;letter-spacing:1px}
.hero-sub em{font-style:normal;color:var(--gold-light)}
.brand{position:absolute;top:420px;width:100%;display:flex;justify-content:center;align-items:center;gap:14px;color:#fff;font-family:"Noto Serif JP",serif;font-size:28px;letter-spacing:2px}
.brand .mark{width:16px;height:16px;border-radius:50%;border:1px solid #fff}
.cta{position:absolute;top:500px;left:50%;transform:translateX(-50%);width:560px;height:60px;border-radius:30px;background:var(--gold);color:#fff;font-size:18px;display:flex;align-items:center;justify-content:center;gap:14px;letter-spacing:1px}
.cta .dot{width:22px;height:22px;border-radius:50%;background:#fff;position:relative}
.cta .dot::after{content:"";position:absolute;left:7px;top:7px;width:6px;height:6px;border-top:2px solid var(--gold);border-right:2px solid var(--gold);transform:rotate(45deg)}

/* profile */
.profile{top:600px;height:230px;background:#efece6}
.profile .photo-main{left:0;top:0;width:620px;height:230px;background:linear-gradient(90deg,#8c8274,#c9bfae 55%,#b0a590)}
.profile-text{position:absolute;left:660px;top:26px}
.profile-text .lead{font-size:15px;color:var(--muted)}
.profile-text .role{font-size:15px;margin-top:6px}
.profile-text .name{font-family:"Noto Serif JP",serif;font-size:34px;font-weight:600;margin-left:8px}
.books{position:absolute;left:660px;top:112px;display:flex;gap:14px}
.books .book{width:100px;height:80px;background:linear-gradient(160deg,#2d3450,#6b7390)}
.books .book:nth-child(2){background:linear-gradient(160deg,#d7d3cc,#a59f93)}
.books .book:nth-child(3){background:linear-gradient(160deg,#3c5a86,#8aa0c0)}
.profile-note{position:absolute;left:660px;top:202px;font-size:11px;color:var(--muted)}

/* intro 01 */
.worries{top:830px;height:550px;background:var(--navy);color:#fff}
.worries .en-label{position:absolute;top:48px;width:100%;color:#d8d6e0}
.worries .section-title{position:absolute;top:90px;width:100%}
.worry-list{position:absolute;top:200px;width:330px;display:flex;flex-direction:column;gap:14px}
.worry-list.left{left:110px}
.worry-list.right{left:760px}
.worry-list li{list-style:none;background:#fff;color:var(--ink);font-size:15px;height:44px;display:flex;align-items:center;padding-left:16px;gap:10px}
.worry-list li::before{content:"";width:12px;height:12px;border:1px solid var(--navy);flex:none}
.worries .figure{left:500px;top:180px;width:200px;height:240px;background:linear-gradient(180deg,#46506e,#2d3452);border-radius:4px}
.worries .closing{position:absolute;top:440px;width:100%;text-align:center;font-size:19px;line-height:1.6;font-weight:500}

/* intro 02 */
.reasons{top:1380px;height:920px;background:var(--navy-mid);color:#fff}
.reasons .en-label{position:absolute;top:58px;width:100%;color:#d8d6e0}
.reasons .section-title{position:absolute;top:100px;width:100%}
.reasons .intro{position:absolute;top:180px;left:200px;width:800px;text-align:center;font-size:14px;line-height:1.9;color:#e6e5ec}
.reason-box{position:absolute;top:300px;width:380px;height:330px;background:#fff;color:var(--ink);padding:40px 30px 20px}
.reason-box.left{left:110px}
.reason-box.right{left:710px}
.reason-box .icon{position:absolute;top:24px;left:30px;width:56px;height:56px}
.reason-box h3{margin-left:72px;font-family:"Noto Serif JP",serif;font-size:21px;line-height:1.45;font-weight:600}
.reason-box p{margin-top:36px;font-size:13.5px;line-height:1.9;color:#444}
.reason-box p em{font-style:normal;color:#c64a3a}
.reasons .figure{left:510px;top:310px;width:180px;height:300px;background:linear-gradient(180deg,#5a6078,#3c425c)}
.reasons .closing{position:absolute;top:730px;width:100%;text-align:center;font-size:21px;line-height:1.6;font-weight:500}

/* professional */
.professional{top:2300px;height:920px;background:var(--cream)}
.professional .photo-main{left:600px;top:0;width:600px;height:920px;background:linear-gradient(135deg,#f2efe9,#dcd6ca 60%,#c5bdaf)}
.professional .en-label{position:absolute;top:100px;left:80px;color:var(--muted);justify-content:flex-start}
.professional .en-label::after{display:none}
.professional h2{position:absolute;top:150px;left:80px;font-family:"Noto Serif JP",serif;font-weight:600;font-size:46px;line-height:1.45;color:var(--ink);letter-spacing:2px}
.thumbs{position:absolute;top:410px;left:80px;display:flex;gap:10px}
.thumbs div{width:110px;height:80px;background:linear-gradient(150deg,#9a9185,#5d5850)}
.professional .body{position:absolute;top:530px;left:80px;width:470px;font-size:14px;line-height:2;color:#444}
.professional .sign{position:absolute;top:770px;left:400px;width:140px;height:50px;background:linear-gradient(90deg,transparent,#cfc9bf,transparent)}

/* strong points */
.merits{top:3220px;height:560px;background:var(--navy);color:#fff}
.merits .en-label{position:absolute;top:58px;width:100%;color:#d8d6e0}
.merits .section-title{position:absolute;top:100px;width:100%;font-size:36px}
.merit{position:absolute;top:190px;width:300px;text-align:center}
.merit:nth-of-type(1){left:110px}
.merit:nth-of-type(2){left:450px}
.merit:nth-of-type(3){left:790px}
.merit .circle{width:120px;height:120px;border-radius:50%;background:#fff;margin:0 auto;display:flex;align-items:center;justify-content:center}
.merit h3{margin-top:22px;font-size:18px;font-weight:700;letter-spacing:1px}
.merit p{margin-top:14px;font-size:13px;line-height:1.85;text-align:left;color:#dcdbe4}

/* cases */
.cases{top:3780px;height:812px;background:#efeeeb}
.cases .en-label{position:absolute;top:50px;width:100%;color:var(--muted)}
.cases .section-title{position:absolute;top:92px;width:100%;font-size:38px;color:var(--ink)}
.case{position:absolute;top:190px;width:300px;height:540px}
.case:nth-of-type(1){left:110px}
.case:nth-of-type(2){left:450px}
.case:nth-of-type(3){left:790px}
.case .before{position:absolute;left:30px;top:0;width:150px;height:160px;background:linear-gradient(160deg,#cfccc6,#8f8b84)}
.case .after{position:absolute;left:0;top:130px;width:300px;height:410px;background:linear-gradient(160deg,#5c5a58,#2f2e2d);border:6px solid #fff}
.tag{position:absolute;background:var(--navy);color:#fff;font-family:"Cormorant Garamond",serif;font-style:italic;font-size:16px;letter-spacing:2px;padding:4px 14px}
.case .before .tag{right:-60px;bottom:40px}
.case .after .tag{left:-6px;top:10px}
</style>
</head>
<body>

<section class="hero">
  <div class="photo" role="img" aria-label="スーツ姿の男性がネクタイを整える手元の写真"></div>
  <p class="hero-tag">ファッションでブランディングを加速させる方法とは?</p>
  <h1 class="hero-title">経営者のための<br>専属スタイリストサービス</h1>
  <p class="hero-sub">既に300名以上が<em>「センスのいい経営者」</em>に変わっています</p>
  <div class="brand"><span class="mark"></span>KAZE styling</div>
  <a class="cta"><span class="dot"></span>初回カウンセリングのお申込みはこちら（毎月3名まで）</a>
</section>

<section class="profile">
  <div class="photo photo-main" role="img" aria-label="アトリエでマネキンの横に立つスタイリストの写真"></div>
  <div class="profile-text">
    <p class="lead">累計5万冊以上の書籍を出版した</p>
    <p class="role">スタイリスト<span class="name">高梨 透</span></p>
  </div>
  <div class="books">
    <div class="book" role="img" aria-label="著書の表紙"></div>
    <div class="book" role="img" aria-label="著書の表紙"></div>
    <div class="book" role="img" aria-label="著書の表紙"></div>
  </div>
  <p class="profile-note">著書は全国の書店・通販サイトにて発売中です。</p>
</section>

<section class="worries">
  <p class="en-label">Introduction.01</p>
  <h2 class="section-title">日々のファッションにこんな悩みはありませんか?</h2>
  <ul class="worry-list left">
    <li>ビジネスでのブランディングに力を入れたい</li>
    <li>講演やセミナーなど人前に立つことが増えてきた</li>
    <li>メディアに注目することが増えてきた</li>
    <li>今の立場にふさわしいファッションに変わりたい</li>
  </ul>
  <div class="photo figure" role="img" aria-label="スーツ姿の男性のイラスト"></div>
  <ul class="worry-list right">
    <li>服装による見た目に変わりたい</li>
    <li>自分のセンスに自信がない</li>
    <li>最適な服選びや店選びに迷ってしまう</li>
    <li>いつまでも魅力的な経営者でありたい</li>
  </ul>
  <p class="closing">1つでも当てはまる方は<br>日々のファッションを見直してみてください。</p>
  <svg class="chevron" style="top:515px" viewBox="0 0 30 18"><path d="M2 2l13 13L28 2" fill="none" stroke="#fff" stroke-width="2"/></svg>
</section>

<section class="reasons">
  <p class="en-label">Introduction.02</p>
  <h2 class="section-title">優秀な経営者がファッションに気を配る理由とは?</h2>
  <p class="intro">近年、ファッションの持つ影響力が見直されています。どんなに商品やサービスが優れていても、第一印象で信頼を得られなければ、その魅力は十分に伝わりません。だからこそ優秀な経営者はファッションを大切にしているのです。</p>
  <div class="reason-box left">
    <svg class="icon" viewBox="0 0 56 56"><circle cx="28" cy="28" r="26" fill="none" stroke="#1e2242" stroke-width="3"/><rect x="25.5" y="13" width="5" height="21" fill="#1e2242"/><rect x="25.5" y="38" width="5" height="5" fill="#1e2242"/></svg>
    <h3>現代の経営者にとってパーソナルブランディングは必須</h3>
    <p>情報があふれる時代において、経営者自身の見た目は企業の顔でもあります。<em>人は見た目で判断されるという事実を前提に、ファッションを意識することが重要です。</em>身だしなみを整えることは信頼を築く第一歩となります。</p>
  </div>
  <div class="photo figure" role="img" aria-label="ジャケットを着た男性のイラスト"></div>
  <div class="reason-box right">
    <svg class="icon" viewBox="0 0 56 56"><circle cx="28" cy="28" r="26" fill="none" stroke="#1e2242" stroke-width="3"/><path d="M20 21a8 8 0 1 1 12 7c-3 2-4 3-4 7" fill="none" stroke="#1e2242" stroke-width="4"/><rect x="25.5" y="38" width="5" height="5" fill="#1e2242"/></svg>
    <h3>最短距離で「センスのいい経営者」になれた理由とは？</h3>
    <p>多忙な経営者ほど自分で服を選ぶ時間はありません。<em>プロのスタイリストに任せることで、最短でふさわしい装いを手に入れています。</em>結果として自信が生まれ、仕事にも良い影響を与えています。</p>
  </div>
  <p class="closing">優れたビジネスマンは<br>ファッションのプロを上手く活用しています。</p>
  <svg class="chevron" style="top:830px" viewBox="0 0 30 18"><path d="M2 2l13 13L28 2" fill="none" stroke="#fff" stroke-width="2"/></svg>
</section>

<section class="professional">
  <div class="photo photo-main" role="img" aria-label="スツールに腰掛けるスーツ姿のスタイリストの写真"></div>
  <p class="en-label">Professional</p>
  <h2>300人以上の経営者の<br>ブランディングを手掛けた<br>ファッションのプロ</h2>
  <div class="thumbs">
    <div role="img" aria-label="セミナー登壇の様子"></div>
    <div role="img" aria-label="顧客とのカウンセリングの様子"></div>
    <div role="img" aria-label="店舗での同行ショッピングの様子"></div>
    <div role="img" aria-label="アトリエの様子"></div>
  </div>
  <p class="body">はじめまして、スタイリストの高梨と申します。<br>私はこれまで300名以上の経営者様に、ファッションを通したブランディングを提供してきました。今では書籍やセミナーなどを通じて、多くの方にその大切さを伝えています。ブランディングを意識したファッションで、経営者の皆様の魅力を最大限に引き出すお手伝いをいたします。</p>
  <div class="sign" role="img" aria-label="スタイリストの手書きサイン"></div>
</section>

<section class="merits">
  <p class="en-label">Strong Points</p>
  <h2 class="section-title">スタイリストを付ける3つのメリットとは?</h2>
  <div class="merit">
    <div class="circle"><svg width="60" height="50" viewBox="0 0 60 50"><path d="M12 2h36l10 14-28 32L2 16z M2 16h56 M22 2l-6 14 14 32 14-32-6-14" fill="none" stroke="#1e2242" stroke-width="2"/></svg></div>
    <h3>パーソナルブランディングができる</h3>
    <p>経営者としての立場や個性を踏まえ、最適なスタイルをご提案します。見た目の印象が変わることで、周囲からの評価も大きく変わります。</p>
  </div>
  <div class="merit">
    <div class="circle"><svg width="40" height="56" viewBox="0 0 40 56"><path d="M4 2h32M4 54h32M8 2c0 16 24 18 24 26S8 38 8 54M32 2c0 16-24 18-24 26s24 10 24 26" fill="none" stroke="#1e2242" stroke-width="2"/></svg></div>
    <h3>時間が節約できる</h3>
    <p>服選びや買い物に費やす時間を大幅に削減できます。空いた時間を本業に充てることで、より価値のある仕事に集中できます。</p>
  </div>
  <div class="merit">
    <div class="circle"><svg width="56" height="56" viewBox="0 0 56 56"><circle cx="28" cy="18" r="10" fill="none" stroke="#1e2242" stroke-width="2"/><path d="M8 54c0-14 9-22 20-22s20 8 20 22" fill="none" stroke="#1e2242" stroke-width="2"/></svg></div>
    <h3>セルフイメージが向上する</h3>
    <p>自分に似合う服を身に付けることで、自然と自信が生まれます。その自信は表情や振る舞いにも表れ、良い循環を生み出します。</p>
  </div>
</section>

<section class="cases">
  <p class="en-label">How They Change</p>
  <h2 class="section-title">おしゃれに変わった方たちをご紹介します</h2>
  <div class="case">
    <div class="before" role="img" aria-label="変身前の男性の写真"><span class="tag">BEFORE</span></div>
    <div class="after" role="img" aria-label="ジャケット姿に変身した男性の写真"><span class="tag">AFTER</span></div>
  </div>
  <div class="case">
    <div class="before" role="img" aria-label="変身前の男性の写真"><span class="tag">BEFORE</span></div>
    <div class="after" role="img" aria-label="スーツ姿に変身した男性の写真"><span class="tag">AFTER</span></div>
  </div>
  <div class="case">
    <div class="before" role="img" aria-label="変身前の男性の写真"><span class="tag">BEFORE</span></div>
    <div class="after" role="img" aria-label="帽子とジャケット姿に変身した男性の写真"><span class="tag">AFTER</span></div>
  </div>
</section>

</body>
</html>
```